Business price tag design for Furniture Business

Hello,

I have developed a tag for a home furniture business and need 1 more creative template. Please see attachment. I need the template to be very appealing.

Requirements:

1.Tag dimensions needs to be about the same as attached tag.
2. Tag design needs to be suitable for a home furniture business.
3. Tag needs to have locations for the following: Item Title, Now Price, Was Price, Product Number.
4. "The black shape at the bottom of attached tag could be removed.

I have no requirements on colors, but something professional is needed, preferably white background to reduce print ink consumption.

Please see attachment for clarification.

Industry/Entity Type

Retail

Font styles to use
Serif
Sans Serif

Requirements
Must have
• Please see Project Description.
Nice to have

```html
<!DOCTYPE html>
<html lang="en">
<head>
<meta charset="utf-8">
<title>Furniture Price Tag</title>
<link rel="stylesheet" href="https://fonts.googleapis.com/css2?family=Libre+Baskerville:wght@400;700&family=Arimo:wght@400;700&display=swap">
<style>
  :root {
    --leather-black: #1e1e1e;
    --leather-black-light: #3a3a3a;
    --leather-red: #8e2430;
    --leather-red-dark: #6a1620;
    --stitch-light: #b9b4ad;
    --stitch-red: #d8a0a6;
    --paper: #ffffff;
    --wine: #7a1f24;
    --ink: #161616;
    --tag-cream: #f7ecc2;
    --tag-cream-dark: #e6d297;
    --white: #ffffff;
  }
  * { box-sizing: border-box; margin: 0; padding: 0; }
  html, body { width: 1200px; height: 2376px; overflow: hidden; background: var(--paper); }
  .price-tag { position: relative; width: 1200px; height: 2376px; background: var(--paper); overflow: hidden; }

  .band { position: absolute; left: 0; width: 1200px; }
  .band--top {
    top: 0; height: 262px;
    background: radial-gradient(ellipse at 50% 30%, var(--leather-black-light), var(--leather-black) 75%);
    box-shadow: 0 10px 18px rgba(0,0,0,0.35);
    z-index: 2;
  }
  .band--middle {
    top: 1288px; height: 504px;
    background: radial-gradient(ellipse at 50% 40%, #a3303c, var(--leather-red-dark) 85%);
    box-shadow: 0 -10px 18px rgba(0,0,0,0.3);
  }
  .band--bottom {
    top: 1792px; height: 584px;
    background: radial-gradient(ellipse at 50% 30%, var(--leather-black-light), var(--leather-black) 75%);
    box-shadow: 0 -8px 16px rgba(0,0,0,0.45);
  }
  .stitch { position: absolute; left: 0; width: 1200px; height: 8px; }

  .item-title {
    position: absolute; left: 0; width: 1200px; top: 318px;
    text-align: center;
    font-family: "Libre Baskerville", serif; font-weight: 400;
    font-size: 150px; line-height: 1; color: var(--wine);
    letter-spacing: 2px;
  }
  .product-number {
    position: absolute; left: 40px; top: 576px;
    font-family: "Arimo", sans-serif; font-weight: 700;
    font-size: 60px; line-height: 1; color: var(--ink);
  }
  .was-label {
    position: absolute; left: 44px; top: 900px;
    font-family: "Arimo", sans-serif; font-weight: 700;
    font-size: 108px; line-height: 1; color: var(--wine);
  }
  .was-price {
    position: absolute; right: 40px; top: 1040px;
    font-family: "Arimo", sans-serif; font-weight: 700;
    font-size: 100px; line-height: 1; color: var(--wine);
  }
  .now-label {
    position: absolute; left: 36px; top: 1380px;
    font-family: "Arimo", sans-serif; font-weight: 400;
    font-size: 140px; line-height: 1; color: var(--white);
    text-shadow: 0 4px 8px rgba(0,0,0,0.55);
  }
  .now-card {
    position: absolute; left: 432px; top: 1390px; width: 748px; height: 358px;
    border-radius: 26px;
    background: radial-gradient(ellipse at 50% 45%, var(--tag-cream) 45%, var(--tag-cream-dark) 100%);
    box-shadow: 0 8px 16px rgba(0,0,0,0.5);
    display: flex; align-items: center; justify-content: center;
  }
  .now-price {
    font-family: "Arimo", sans-serif; font-weight: 700;
    font-size: 132px; line-height: 1; color: var(--ink);
  }
  .delivery {
    position: absolute; left: 0; width: 1200px; top: 1990px;
    text-align: center;
    font-family: "Arimo", sans-serif; font-weight: 700;
    font-size: 116px; line-height: 158px; color: var(--white);
  }
</style>
</head>
<body>
<main class="price-tag">
  <div class="band band--top">
    <svg class="stitch" style="top:216px" viewBox="0 0 1200 8"><line x1="0" y1="4" x2="1200" y2="4" stroke="var(--stitch-light)" stroke-width="4" stroke-dasharray="22 12"/></svg>
  </div>

  <h1 class="item-title">ITEM TITLE</h1>
  <p class="product-number">PRODUCT #</p>
  <p class="was-label">WAS:</p>
  <p class="was-price">$0000.00</p>

  <div class="band band--middle">
    <svg class="stitch" style="top:30px" viewBox="0 0 1200 8"><line x1="0" y1="4" x2="1200" y2="4" stroke="var(--stitch-red)" stroke-width="4" stroke-dasharray="22 12"/></svg>
    <svg class="stitch" style="top:470px" viewBox="0 0 1200 8"><line x1="0" y1="4" x2="1200" y2="4" stroke="var(--stitch-red)" stroke-width="4" stroke-dasharray="22 12"/></svg>
  </div>
  <p class="now-label">NOW</p>
  <div class="now-card"><p class="now-price">$0000.00</p></div>

  <div class="band band--bottom">
    <svg class="stitch" style="top:54px" viewBox="0 0 1200 8"><line x1="0" y1="4" x2="1200" y2="4" stroke="var(--stitch-light)" stroke-width="4" stroke-dasharray="22 12"/></svg>
  </div>
  <p class="delivery">NEED DELIVERY?<br>NO PROBLEM!</p>
</main>
</body>
</html>
```